Halvern Partners M&A Email Newsletter Design

Halvern Partners is a Marketing/Consulting/M&A company and we want to find a graphic designer experienced in newsletter design. Please visit our website for more information and to see our logo. We would like the color scheme of the newsletter to reflect our colors of blue, yellow, and dark gray (see website for visual representation). The newsletter will focus on detailing M&A news in the market. Please reach out if you have any questions. https://www.halvernpartners.example/

Industry/Entity Type

Marketing

Font styles to use
Serif
Sans Serif

Colors
0456a4
ffc214
ffcf3e

Requirements
Must have
• Halvern Partners' Color Scheme: Yellow, Blue, Dark Gray (see website)
Professional economics newsletter
Should not have
• Strange/hard to read fonts

```html
<!DOCTYPE html>
<html lang="en">
<head>
<meta charset="utf-8">
<title>Halvern Partners – M&amp;A News</title>
<link href="https://fonts.googleapis.com/css2?family=Montserrat:wght@400;500;600;700&family=Merriweather:ital,wght@0,400;1,400&display=swap" rel="stylesheet">
<style>
:root{
  --blue:#1f66b0;
  --blue-deep:#0456a4;
  --blue-soft:#5b8fc7;
  --yellow:#ffc214;
  --yellow-light:#ffcf3e;
  --yellow-dark:#e0a800;
  --gray-bg:#f0f0f0;
  --ink:#2b2b2b;
  --muted:#7a7a7a;
  --white:#ffffff;
}
*{margin:0;padding:0;box-sizing:border-box}
html,body{width:1200px;height:1200px;overflow:hidden;background:var(--white)}
.canvas{position:relative;width:1200px;height:1200px;overflow:hidden}
.newsletter{position:absolute;left:532px;top:19px;width:576px;height:4688px;transform:scale(.25);transform-origin:0 0;background:var(--white);font-family:"Merriweather",Georgia,serif;color:var(--ink)}
.block{position:absolute;left:0;width:576px;overflow:hidden}
.sans{font-family:"Montserrat",Arial,sans-serif}
p{font-size:11.5px;line-height:16.5px;margin-bottom:12px}
.kicker{font-family:"Montserrat",Arial,sans-serif;font-size:11px;line-height:14px;text-transform:uppercase;color:var(--ink);margin-bottom:4px;font-weight:500}
.placeholder{position:absolute}
.btn{display:inline-block;font-family:"Montserrat",Arial,sans-serif;font-weight:700;font-size:11px;letter-spacing:.3px;padding:6px 9px;text-transform:uppercase}

/* header */
.masthead{top:0;height:248px;background:var(--gray-bg)}
.masthead .meta{position:absolute;top:34px;left:70px;right:110px;display:flex;justify-content:space-between;font-family:"Montserrat",Arial,sans-serif;font-size:8px;font-weight:600}
.brand{position:absolute;top:96px;left:180px;display:flex;align-items:center;gap:8px}
.brand-name{font-family:"Montserrat",Arial,sans-serif;font-weight:500;font-size:29px;color:var(--yellow)}
.brand-mark{width:12px;height:12px;background:var(--blue-deep)}
.tagline{position:absolute;top:137px;left:181px;font-family:"Montserrat",Arial,sans-serif;font-size:9px;font-weight:600;letter-spacing:.6px;color:var(--muted)}
.issue-title{position:absolute;top:175px;left:0;width:576px;text-align:center;font-family:"Montserrat",Arial,sans-serif;font-weight:600;font-size:28px;color:#555}

/* lead */
.hero{top:248px;height:210px}
.lead{top:471px;height:423px}
.lead .copy{position:absolute;left:25px;top:0;width:325px}
.headline{font-family:"Montserrat",Arial,sans-serif;font-weight:700;font-size:16px;line-height:21px;text-transform:uppercase;color:var(--ink)}
.subhead{font-family:"Montserrat",Arial,sans-serif;font-weight:500;font-size:11.5px;line-height:17px;text-transform:uppercase;color:var(--muted);margin:4px 0 8px}
.byline{font-style:italic;font-size:9.5px;color:var(--muted);margin-bottom:10px}
.contents{position:absolute;right:0;top:0;width:203px;height:423px;background:var(--yellow);padding:26px 14px}
.contents h3{font-family:"Montserrat",Arial,sans-serif;font-size:10px;font-weight:700;padding-bottom:10px;border-bottom:1px solid var(--yellow-light);color:#3a3a3a}
.contents li{list-style:none;font-family:"Montserrat",Arial,sans-serif;font-size:10.5px;line-height:13.5px;font-weight:600;color:#3a3a3a;padding:24px 0 14px;border-bottom:1px solid var(--yellow-light);text-transform:uppercase}

/* purpose band */
.purpose{top:894px;height:213px;background:var(--blue-deep);color:var(--white)}
.purpose h2{text-align:center;font-family:"Montserrat",Arial,sans-serif;font-size:18px;font-weight:600;letter-spacing:.4px;margin-top:38px}
.purpose .cols{display:flex;gap:40px;padding:30px 36px 0}
.purpose .cols p{font-family:"Montserrat",Arial,sans-serif;font-size:9px;line-height:15px;margin:0;flex:1}

/* strategy continued */
.strategy{top:1107px;height:708px}
.strategy .left{position:absolute;left:25px;top:155px;width:255px}
.strategy .right{position:absolute;left:306px;top:14px;width:245px}
.callout-text{position:absolute;left:395px;top:510px;width:150px;text-align:center;font-family:"Montserrat",Arial,sans-serif;font-weight:600;font-size:17px;line-height:27px;color:var(--blue-deep)}

/* ebook */
.ebook{top:1815px;height:519px;background:var(--yellow)}
.cover{position:absolute;left:25px;top:88px;width:168px;height:350px;background:var(--blue-soft);color:var(--white);text-align:center;padding:10px 10px}
.cover-brand{font-family:"Montserrat",Arial,sans-serif;font-size:12px;font-weight:600;color:var(--yellow-light);margin-bottom:12px}
.cover-title{font-family:"Montserrat",Arial,sans-serif;font-size:19px;line-height:21px;font-weight:500;text-transform:uppercase}
.cover-note{font-family:"Montserrat",Arial,sans-serif;font-size:7px;font-weight:700;margin:10px 0 6px;color:var(--yellow-light)}
.ebook .copy{position:absolute;left:215px;top:38px;width:318px}
.ebook .btn{background:var(--blue-deep);color:var(--white)}

/* buying */
.buying{top:2544px;height:1419px}
.buying .intro{position:absolute;left:35px;top:0;width:520px}
.buying .left{position:absolute;left:35px;top:70px;width:245px}
.buying .right{position:absolute;left:306px;top:135px;width:250px}
ol{padding-left:18px}
ol li{font-size:11.5px;line-height:16.5px;margin-bottom:12px}
.quote{position:absolute;left:306px;top:410px;width:270px;height:168px;background:var(--blue);color:var(--white);padding:20px 24px 0 24px;text-align:center;font-family:"Montserrat",Arial,sans-serif;font-style:italic;font-size:10.5px;line-height:21px}

/* value */
.value-photo{top:3975px;height:177px}
.value{top:4152px;height:343px;background:var(--blue-soft);color:var(--white);padding:30px 35px}
.value h2{font-family:"Montserrat",Arial,sans-serif;font-size:15px;line-height:21px;font-weight:700;text-transform:uppercase;margin-bottom:14px}
.value p{font-family:"Montserrat",Arial,sans-serif;font-size:9.5px;line-height:14px;margin-bottom:10px}
.value .lede{font-weight:600;font-size:10.5px}
.value .fine{font-size:8px;line-height:12px}
.value .btn{background:var(--yellow);color:var(--white);font-size:10px}

/* footer */
.footer{top:4495px;height:193px}
.office{position:absolute;top:18px;font-family:"Montserrat",Arial,sans-serif;font-size:8.5px;line-height:12px;color:var(--blue-deep)}
.office strong{display:block;font-weight:600;margin-bottom:8px;text-decoration:underline}
</style>
</head>
<body>
<div class="canvas">
<article class="newsletter">

  <header class="block masthead">
    <svg width="576" height="248" style="position:absolute;left:0;top:0">
      <polygon points="0,105 162,178 0,248" fill="var(--yellow)"/>
      <polygon points="0,248 162,178 60,248" fill="var(--yellow-dark)"/>
      <polygon points="576,138 480,193 576,248" fill="var(--blue)"/>
    </svg>
    <div class="meta"><span>September 15, 2020</span><span>Issue 1</span></div>
    <div class="brand"><span class="brand-name">Halvern Partners</span><span class="brand-mark"></span></div>
    <div class="tagline">GUIDING AGENCY OWNERS</div>
    <h1 class="issue-title">M&amp;A News</h1>
  </header>

  <section class="block hero">
    <div class="placeholder" role="img" aria-label="Illustration of a businessman climbing rising blue bar chart steps with a yellow growth arrow" style="left:100px;top:0;width:380px;height:205px;background:linear-gradient(90deg,#ffffff 0%,#dbe7f4 40%,#9fc0e3 75%,#ffe08a 100%)"></div>
  </section>

  <section class="block lead">
    <div class="copy">
      <h2 class="headline">Agency Owners – When the M&amp;A Market Rebounds, Will You Be Ready?</h2>
      <div class="subhead">For M&amp;A tomorrow, establish your strategy and prepare today</div>
      <div class="byline">by Dana Whitfield</div>
      <p>M&amp;A will rebound. Be ready.</p>
      <p>While M&amp;A activity for communications firms has diminished dramatically if not shut down completely, now is the time to reassess your M&amp;A strategy. Whether buyer or seller, you should ensure that you're best prepared to act when the market rebounds.</p>
      <div class="kicker">Strategic considerations for buyers</div>
      <p>Your acquisition strategy must align with the long-term needs of your agency and guide against pursuing ill-fitting firms that would divert valuable resources and strain the overall business.</p>
      <p>You should review this strategy periodically, adjusting to changes in the business and industry so that you</p>
    </div>
    <aside class="contents">
      <h3>IN THIS ISSUE</h3>
      <ul>
        <li>What agency owners need to know about buying another agency</li>
        <li>Vital strategies you must consider before selling your digital agency</li>
        <li>What is your agency worth? And why it's important to know</li>
      </ul>
    </aside>
  </section>

  <section class="block purpose">
    <h2>WHY HALVERN PARTNERS EXISTS</h2>
    <div class="cols">
      <p>Halvern Partners exists to help the owners of independent marketing communications agencies achieve their life ambitions and maximize the value of their lives' work. Our team of former agency leaders and owners</p>
      <p>focus their deep experience on implementing proven proprietary methodologies across our three practices of agency performance, owner exit planning and M&amp;A transactions in order to drive owner and agency success.</p>
    </div>
  </section>

  <section class="block strategy">
    <div class="placeholder" role="img" aria-label="Photo of shoes standing on pavement above a red painted START HERE line" style="left:0;top:0;width:278px;height:138px;background:linear-gradient(180deg,#7d7d7d 0%,#a3a3a3 55%,#b01d1d 78%,#c52222 100%)"></div>
    <div class="left">
      <p>remain on the right course. Also, new opportunities may present themselves that compel you to rethink the current criteria and adjust if needed.</p>
      <p>Any significant changes to your M&amp;A strategy should result from a thoughtful process. Whatever your established strategy may be, the acquisition team should fully understand it and agree across the board.</p>
      <div class="kicker">We propose the following six considerations for developing a disciplined and strategic pursuit of acquisition targets:</div>
      <p>What is the desired range of services involved? Are you looking to enhance existing capabilities or invest in new, complementary services? Have you assessed the market to understand its direction and competitor activity?</p>
      <p>What are the preferred industry sectors? Do you want to serve new industry categories?</p>
      <p>What are the preferred and minimum revenue levels? Obviously, this targeting depends upon the level of capital available. However, you should stay within a compatible revenue range for your firm as</p>
    </div>
    <div class="right">
      <p>well as pursue candidate businesses with a history of growth.</p>
      <p>What are the target or minimum profit margins? Unless you can assure course correction of an underperforming business, seek businesses with margins in the 20%+ range that demonstrate consistent profits at this level. Pursue earnings-enhancing businesses as a first course of action.</p>
      <p>Are there any specific geographic locations to pursue? Also, should you expand in existing markets or pursue new ones?</p>
      <p>What are the inherent cultural and core values that define your business? Have you identified these criteria and a process to compare your firm with candidate businesses? Spend time on chemistry to assess and assure the proper fit. Many deals fail due to conflicting value sets between businesses.</p>
    </div>
    <svg width="576" height="708" style="position:absolute;left:0;top:0">
      <polygon points="576,392 306,576 576,708" fill="var(--yellow)"/>
    </svg>
    <div class="callout-text">M&amp;A WILL REBOUND.<br>BE READY.</div>
  </section>

  <section class="block ebook">
    <div class="cover">
      <div class="cover-brand">Halvern Partners</div>
      <div class="cover-title">Vital strategies you must consider before selling your digital agency</div>
      <div class="cover-note">PLUS KEY TACTICS TO HELP MAXIMIZE YOUR EARN-OUT</div>
      <div role="img" aria-label="Photo of a modern office lounge with yellow chairs" style="width:148px;height:90px;margin:0 auto;background:linear-gradient(180deg,#3b4a5c 0%,#6b6a55 60%,#c9a23a 100%)"></div>
    </div>
    <div class="copy">
      <h2 class="headline">Vital strategies you must consider before selling your digital agency</h2>
      <p style="margin-top:6px">Is now the right time to sell your digital agency?</p>
      <p>You've worked hard to build your digital agency and run a successful business. Your success took sacrifice, conviction and a relentless belief in yourself. But, eventually we all move on. Maybe you want to pursue another venture. Perhaps you've built a great reputation and you want to capitalize on it. Or, maybe you're just burnt out from jumping through aiming hoops each day for clients.</p>
      <p>Maybe you simply want to enjoy life for a change.</p>
      <p>Whatever the reason, you need to plan early to maximize your earn out. There are several key phases of the sale process that must be executed in harmony. Otherwise you risk giving away your firm for less than it's worth. All of the partners here at Halvern Partners have owned, managed, bought and/or sold several agencies. So, we'd like to share our experience with you so you can get the most out of your business.</p>
      <span class="btn">Download full e-book</span>
    </div>
  </section>

  <section class="block" style="top:2334px;height:205px">
    <div class="placeholder" role="img" aria-label="Photo of a hand pulling a block from a wooden block tower" style="left:0;top:0;width:576px;height:205px;background:linear-gradient(90deg,#d9dde2 0%,#9aa4b0 35%,#c8905a 62%,#e9e4dc 100%)"></div>
  </section>

  <section class="block buying">
    <div class="intro">
      <h2 class="headline">What agency owners need to know about buying another agency</h2>
      <div class="subhead">Buying an agency requires managing risk.</div>
    </div>
    <div class="left">
      <div class="kicker">Thinking of buying an agency? Here are some important considerations.</div>
      <p>Buying an agency to spur your agency's growth can be a brilliant and exciting strategic move. However, it's also a very complex process filled with risks and uncertainties for the untrained agency buyer. A mistake could be costly financially and damage your culture. Most independent agencies seeking to acquire another independent agency cannot afford to make a mistake.</p>
      <p>As a buyer, you need to apply a proven risk assessment process to maximize the chances of a positive outcome. You must clearly define your goals and the characteristics of the acquisition you seek so you know when to move forward or when to walk away. Once you decide to move ahead, the process can be time-consuming and complicated so having an experienced partner to guide you is important.</p>
      <div class="kicker">How to avoid the most common pitfalls of buying an agency.</div>
      <p>Based on our recent experience, here are ten of the most important considerations for buyers:</p>
      <ol>
        <li>Why do you want to acquire in the first place? What do you hope this transaction will add to your firm? How strong is the strategic fit? Be honest. Be specific.</li>
        <li>Develop clear criteria in advance to help identify the optimal seller. Establishing seller criteria will be very helpful in assessing the strategic fit up front and then during the inevitable stress and emotions of making the offer and negotiating the deal.</li>
        <li>Be patient. Understand that buying an agency can be a long and expensive process. Both the buyer and seller have businesses to run in addition to managing the deal. The seller may be involved with other buyers, too. On average, the M&amp;A process takes 8-12 months. Overall costs for advisors, lawyers and CPAs can easily be $150,000 or more.</li>
        <li>You must understand how to determine the seller's fair market value. This is in part a detailed financial analysis best conducted by experienced experts. It's also an objective assessment of critically important qualitative factors including the strength and stability of the seller's management team, business development capabilities and more.</li>
        <li>Ensure your acquisition can be a going concern without the selling owner. Does the seller's firm have enough senior talent depth to service accounts, win new business and manage the team should the selling owner exit the business someday? Depth of the second-tier team is the best protection for ensuring an acquisition can survive the eventual departure of its original owner.</li>
      </ol>
    </div>
    <div class="right">
      <ol start="6">
        <li>Cultural compatibility is a must. Integrating the wrong culture into your agency can be a disaster for everyone. Will the acquired agency be able to excel within the vision, sense of purpose and operations of your organization? Conducting a cultural assessment will help you to identify the right seller. Your future profitability (and happiness) will depend on it.</li>
        <li>What's your plan for integrating the acquisition into your organization? Will it be a free-standing entity retaining its own name or absorbed</li>
      </ol>
    </div>
    <div class="quote">We do not simply manage a transaction. We will be your partner in helping to preserve your firm's culture and your personal interest… and never do a deal just for the sake of doing a deal.</div>
    <svg width="576" height="600" style="position:absolute;left:0;top:0;pointer-events:none">
      <polygon points="576,415 576,455 548,435" fill="var(--yellow)"/>
      <polygon points="306,535 306,578 330,556" fill="var(--blue-soft)"/>
    </svg>
    <div class="right" style="top:598px">
      <p style="padding-left:18px">into your firm? Exactly how will that work? How will you ensure that clients won't leave from either your firm or the seller's? Who will be doing what after the deal is done? Are the seller's most important people locked in?</p>
      <ol start="8">
        <li>Don't limit your options by not having alternative deals to consider. Sellers will have different reasons and levels of urgency for selling. A deeper review of your opportunities can identify a better fit, lower price, or both.</li>
        <li>Be painstakingly precise in your due diligence. Ensure that the seller's client/agency contracts, staff information (especially for key talent) and financial statements are well organized. In fact, you can find out a lot about the seller based on the quality and completeness of their records.</li>
        <li>Be just as careful with the transaction documents. The documents required to reflect the transaction and protect you as buyer include detailed sales and employment agreements. These agreements include various provisions that define the rights of both parties, the financial aspects of the deal and many protections to safeguard the buyer's business.</li>
      </ol>
      <p>There are many considerations in buying another agency. At Halvern Partners, we help buyers define their personal and stakeholder goals, develop valuation ranges for target acquisitions, find the right seller based on your goals and negotiate a reasonable price.</p>
    </div>
  </section>

  <section class="block value-photo">
    <div class="placeholder" role="img" aria-label="Photo of a businessman holding a tablet with a blue bar chart rising from it" style="left:35px;top:0;width:488px;height:177px;background:linear-gradient(90deg,#1d3d66 0%,#35598a 45%,#8fd0f5 65%,#1aa7ec 100%)"></div>
  </section>

  <section class="block value">
    <h2>What is your agency worth? And why it's important to know</h2>
    <p class="lede">One day, you'll want all your life's work to pay off.</p>
    <p>You've invested blood, sweat and tears into your agency over the years. And, you've made many sacrifices to achieve success. Eventually it will be time to capitalize on your investment—so you can enjoy a new chapter in life.</p>
    <p class="fine">In exit planning and M&amp;A transactions, most advisors will follow an agency's preliminary valuation and five-year cash flow forecast to assess its value. And that value determines the owner's potential sales price and breadth of potential exit options.</p>
    <p class="fine">If the owner does not take steps to maximize agency value in the years leading up to a sale or exit, then he/she may not receive the full potential value for the agency. Yet, a valuation costs big money. So naturally you need to know if this is vital.</p>
    <span class="btn">Download full e-book</span>
  </section>

  <footer class="block footer">
    <div class="office" style="left:138px"><strong>NEW YORK</strong>118 W. 74th St. Suite 4B<br>New York, NY 10023</div>
    <div class="office" style="left:306px"><strong>CALIFORNIA</strong>562 N. Linden Dr. Suite 110<br>Beverly Hills, California 90210</div>
    <svg width="576" height="193" style="position:absolute;left:0;top:0">
      <polygon points="78,63 0,193 160,193" fill="var(--blue)"/>
      <polygon points="576,33 365,193 576,193" fill="var(--yellow)"/>
      <polygon points="576,33 470,193 576,193" fill="var(--yellow-dark)" opacity=".45"/>
    </svg>
  </footer>

</article>
</div>
</body>
</html>
```